meadowlight balance care (MBC)

I need to build a website for my therapy business.
There are two parts to the website
on the landing page; they choose whether they are therapists making a referral or patients needing more information.
After that, they are taken to their respective pages.
There is the textual information and a referral form on the therapist page, and on the patient page, the text is a bit different, and there will be a booking page on the patient page.
Visually minimal, it's a therapeutic website. I want it clean, clinical, and modern
colors: greenish blue or maybe orangish
PHP/html code
Updates

Hi everyone
I'm very sorry for the lack of responses to your designs. I am trying to work it out, but this platform has been a challenge for me.
I appreciate everyone's efforts, and I am unsure how to rate designs and move forward with the ones I like. There is a 5-star rating, but I don't understand how I'm supposed to politely say that it is not it without feeling like I'm going to affect someone's future rating negatively.
Please understand me. Thank you

Designs look the same

Target Market(s)

therapy and stress management

Industry/Entity Type

stress management therapy

Coding

Coded - Design and coding required

Number of Pages Required

5+ page

Font styles to use
Serif

Colors
0094D4
00A9DD
6FCCEA
C7EBF8
E9F6FB
00AB8E
00BBA5
67D7C9
C6EFE9
E9F9F6

Requirements
Must have
• landing page that that have 2 options. one for therapist another for patient

```html
<!DOCTYPE html>
<html lang="en">
<head>
<meta charset="utf-8">
<title>Meadowlight Balance Care</title>
<link href="https://fonts.googleapis.com/css2?family=Poppins:wght@400;500;600;700&family=Cormorant+Garamond:ital,wght@1,500&display=swap" rel="stylesheet">
<style>
:root{
  --teal:#00BBA5;
  --teal-dark:#00AB8E;
  --teal-soft:#67D7C9;
  --teal-pale:#E9F9F6;
  --orange:#F7941D;
  --ink:#1f2328;
  --text:#6b6f73;
  --grey-bg:#f2f2f2;
  --cream:#fffaf7;
  --peach:#f6c9b4;
  --footer:#2b3a44;
  --white:#ffffff;
  --line:#d9dcdf;
}
*{box-sizing:border-box;margin:0;padding:0}
html,body{width:1200px;height:3000px;overflow:hidden;background:var(--white)}
body{font-family:'Poppins',sans-serif;color:var(--ink);position:relative}
.section{position:relative;width:1200px;overflow:hidden}
.abs{position:absolute}
.script{font-family:'Cormorant Garamond',serif;font-style:italic;color:var(--teal);font-size:19px}
.h2{font-weight:600;font-size:27px;color:var(--ink)}
.center{text-align:center;left:0;right:0}
.para{font-size:10px;line-height:17px;color:var(--text)}
.btn{display:inline-block;background:var(--teal);color:var(--white);font-size:10px;font-weight:500;letter-spacing:.3px;padding:8px 16px;text-transform:uppercase}
.btn-outline{display:inline-block;border:1.5px solid var(--teal);color:var(--teal);font-size:10px;padding:7px 15px;text-transform:uppercase}
.ticks{list-style:none;font-size:9.5px;color:var(--text)}
.ticks li{margin-bottom:8px;padding-left:15px;position:relative}
.ticks li::before{content:"";position:absolute;left:2px;top:2px;width:4px;height:7px;border:solid var(--teal);border-width:0 1.5px 1.5px 0;transform:rotate(45deg)}
.chev{position:absolute;width:14px;height:14px;border:solid #9aa0a4;border-width:0 1.5px 1.5px 0}
.chev.left{transform:rotate(135deg)}
.chev.right{transform:rotate(-45deg)}

/* header + hero */
.hero{height:404px;background:var(--cream)}
.topbar{top:8px;right:160px;font-size:9px;color:var(--ink);display:flex;gap:10px;align-items:center}
.dots{display:flex;gap:6px}
.dots span{width:8px;height:8px;border-radius:50%;background:var(--ink)}
.brand{top:22px;left:158px;display:flex;align-items:center;gap:8px;height:34px}
.brand-mark{width:22px;height:22px;border-radius:50%;background:var(--teal)}
.brand-name{font-weight:600;font-size:28px;line-height:34px;letter-spacing:6px;color:var(--ink)}
.brand-sub{position:absolute;top:58px;left:158px;font-size:7px;letter-spacing:1px;color:var(--orange);font-weight:500;text-transform:uppercase}
.nav{top:30px;left:390px;display:flex;align-items:center;gap:31px;font-size:10px;font-weight:500;text-transform:uppercase}
.nav .btn{margin-left:-6px}
.hero-tag{top:128px;left:158px}
.hero-title{top:150px;left:158px;font-size:36px;font-weight:700}
.hero-title em{font-style:normal;color:var(--orange)}
.hero-text{top:206px;left:158px;width:290px}
.hero-btn{top:256px;left:158px}
.path-choice{top:300px;left:158px;display:flex;gap:12px}
.path{width:180px;background:var(--white);border-left:3px solid var(--teal);padding:9px 12px;box-shadow:0 2px 8px rgba(0,0,0,.06)}
.path b{display:block;font-size:11px;font-weight:600;color:var(--ink)}
.path span{font-size:9px;color:var(--text)}
.path.patient{border-left-color:var(--orange)}

/* welcome */
.welcome{height:382px}
.who-img{left:184px;top:145px;width:408px;height:172px;background:linear-gradient(135deg,#cfd6d8,#8c9499 60%,#5d646a)}
.who-frame{left:170px;top:158px;width:408px;height:172px;border-left:8px solid var(--orange);border-bottom:8px solid var(--orange)}
.who{left:626px;top:145px;width:420px}
.who h3{font-size:13px;font-weight:600;margin-bottom:8px}
.who-cols{display:flex;gap:20px;margin-top:12px}

/* treatments */
.treat{height:382px;background:var(--grey-bg)}
.card{top:114px;width:205px;height:180px;background:var(--white);border-bottom:3px solid var(--teal);padding:5px;text-align:center}
.card .pic{height:102px}
.card h4{font-size:11px;font-weight:600;line-height:13px;margin-top:12px}
.arrow-line{display:block;margin:9px auto 0;width:32px;height:2px;background:var(--orange);position:relative}
.arrow-line::after{content:"";position:absolute;right:0;top:-3px;width:6px;height:6px;border:solid var(--orange);border-width:1.5px 1.5px 0 0;transform:rotate(45deg)}

/* therapist */
.therapist{height:472px}
.doc-pill{left:312px;top:128px;width:172px;height:272px;border-radius:86px;background:linear-gradient(180deg,#f0dcdf,#d9bfc5)}
.doc{left:596px;top:144px;width:360px}
.doc h3{font-size:14px;font-weight:600}
.doc .role{font-family:'Cormorant Garamond',serif;font-style:italic;font-size:13px;color:var(--text);margin-bottom:12px}

/* success */
.success{height:346px;background:var(--orange)}
.success-photo{left:0;top:0;width:1200px;height:186px;background:linear-gradient(90deg,#5fae9f,#73b7ab 45%,#5c9e93)}
.story{left:385px;top:134px;width:430px;height:132px;background:var(--white);text-align:center;padding:44px 36px 0}
.avatar{left:578px;top:112px;width:46px;height:46px;border-radius:50%;background:linear-gradient(135deg,#e9b89d,#b5754f);border:3px solid var(--white)}
.stats{top:282px;left:0;right:0;display:flex;justify-content:center;gap:100px;color:var(--white);text-align:center}
.stats b{display:block;font-size:18px;font-weight:600}
.stats span{font-family:'Cormorant Garamond',serif;font-style:italic;font-size:11px}
.bubble{border:1.5px solid rgba(255,255,255,.5);border-radius:50%}

/* news */
.news{height:382px}
.post{top:72px;width:281px}
.post .pic{height:153px;background:linear-gradient(135deg,#c9d4d4,#b6a17a 55%,#6f6f63);position:relative}
.date{position:absolute;left:8px;top:12px;width:36px;height:40px;background:var(--teal);color:var(--white);font-size:9px;text-align:center;padding-top:6px;line-height:12px}
.post h4{font-size:12px;font-weight:600;line-height:14px;margin:10px 0 6px}
.post .more{color:var(--orange)}

/* appointment */
.appoint{height:406px}
.services{left:160px;top:40px;width:281px;height:280px;background:linear-gradient(180deg,var(--teal),var(--teal-soft));padding:24px 24px;color:var(--white)}
.services h3{font-size:20px;font-weight:600;margin-bottom:10px}
.svc{display:flex;align-items:center;gap:16px;padding:10px 0;border-bottom:1px solid rgba(255,255,255,.35);font-size:13px;font-weight:500;line-height:15px}
.svc:last-child{border-bottom:none}
.svc i{width:30px;height:30px;border:1.5px solid var(--white);border-radius:50%}
.form{left:534px;top:40px;width:508px}
.form h3{font-size:24px;font-weight:600;margin-bottom:22px}
.row{display:flex;gap:20px;margin-bottom:18px}
.field{flex:1;height:26px;border:1px solid var(--line);font-size:9px;color:var(--text);padding:7px 10px}
.field.tall{height:64px}

/* footer */
.footer{height:226px;background:var(--footer);color:#c9d1d6}
.footer h5{font-size:13px;font-weight:600;color:var(--white);margin-bottom:12px}
.footer ul{list-style:none;font-size:9px;line-height:19px}
.f-brand{left:158px;top:30px}
.f-contact{left:158px;top:98px;font-size:9px;line-height:13px}
.f-contact p{margin-bottom:10px;padding-left:20px;position:relative}
.f-contact p::before{content:"";position:absolute;left:0;top:2px;width:8px;height:8px;border-radius:50%;background:var(--white)}
.soc li{display:flex;align-items:center;gap:8px;line-height:24px;font-size:11px}
.soc li::before{content:"";width:9px;height:9px;border-radius:50%;background:var(--white)}
.copy{left:0;right:0;bottom:8px;text-align:center;font-size:8px;color:#c9d1d6}
</style>
</head>
<body>

<header class="section hero">
  <div class="abs topbar"><span>&#9743; +1 555 010 2040</span><span>|</span><span>&#9993; info@mbc.care</span><span class="dots"><span></span><span></span><span></span><span></span></span></div>
  <div class="abs brand"><span class="brand-mark"></span><span class="brand-name">MBC</span></div>
  <div class="brand-sub">meadowlight balance care</div>
  <nav class="abs nav"><span>Home</span><span>About us</span><span>Staff</span><span>Patients</span><span>Treatment &#9662;</span><span>Contact us</span><span class="btn">Book an appointment</span></nav>
  <p class="abs script hero-tag">Get your life style back</p>
  <h1 class="abs hero-title">Feel the <em>RELEXING</em> sensation</h1>
  <p class="abs para hero-text">Lorem ipsum dolor sit amet, consectetur adipiscing elit, sed do eiusmod tempor incididunt ut labore et dolore magna aliqua.</p>
  <span class="abs btn-outline hero-btn">Book an appointment</span>
  <div class="abs path-choice">
    <div class="path"><b>I am a therapist</b><span>Make a referral</span></div>
    <div class="path patient"><b>I am a patient</b><span>Get information &amp; book</span></div>
  </div>
  <svg class="abs" style="left:690px;top:50px" width="400" height="354" viewBox="0 0 400 354">
    <circle cx="200" cy="178" r="172" fill="none" stroke="#9aa0a4" stroke-dasharray="5 5"/>
    <circle cx="165" cy="200" r="148" fill="var(--peach)"/>
    <defs><linearGradient id="heroPhoto" x1="0" y1="0" x2="0" y2="1"><stop offset="0" stop-color="#f3d9cc"/><stop offset=".55" stop-color="#9fb4bd"/><stop offset="1" stop-color="#3a3a3a"/></linearGradient></defs>
    <rect role="img" aria-label="Photo of a calm woman sitting beside balancing stones" x="120" y="30" width="170" height="300" rx="20" fill="url(#heroPhoto)"/>
  </svg>
</header>

<section class="section welcome">
  <p class="abs script center" style="top:0;text-align:center">Welcome to</p>
  <h2 class="abs h2 center" style="top:20px;text-align:center">Meadowlight Balance Care</h2>
  <p class="abs para" style="top:62px;left:340px;width:520px;text-align:center">Lorem ipsum dolor sit amet, consectetur adipiscing elit, sed do eiusmod tempor incididunt ut labore et dolore magna aliqua. Lorem ipsum dolor sit amet, consectetur adipiscing elit, sed do eiusmod tempor incididunt ut labore et dolore magna aliqua.</p>
  <div class="abs who-frame"></div>
  <div class="abs who-img" role="img" aria-label="Therapy group session in a bright room"></div>
  <div class="abs who">
    <h3>Who we are</h3>
    <p class="para">Lorem ipsum dolor sit amet, consectetur adipiscing elit, sed do eiusmod tempor incididunt ut labore et dolore magna aliqua. Lorem ipsum dolor sit amet, consectetur adipiscing elit, sed do eiusmod tempor incididunt ut labore et dolore magna aliqua.</p>
    <div class="who-cols">
      <ul class="ticks"><li>Drug Abuse Prevention and Treatment</li><li>Assessment Consultation &amp; Treatment</li><li>Biofeedback and Health Psychology</li><li>Child, Adolescent and Family Services</li></ul>
      <ul class="ticks"><li>Healthy Lifestyles</li><li>Guided Self-Change</li><li>Intensive Psychodynamic Therapy</li><li>Neuropsychology Assessment Center</li></ul>
    </div>
    <span class="btn" style="margin-top:6px">Read more about us</span>
  </div>
</section>

<section class="section treat">
  <p class="abs script center" style="top:44px;text-align:center">How we can help</p>
  <h2 class="abs h2 center" style="top:64px;text-align:center">Our Treatments</h2>
  <span class="chev left" style="left:210px;top:196px"></span>
  <span class="chev right" style="left:980px;top:196px"></span>
  <div class="abs card" style="left:260px"><div class="pic" role="img" aria-label="Woman meditating with hands together" style="background:linear-gradient(135deg,#dfe3e6,#8a8f94)"></div><h4>Cognitive Behavioral Therapy<br>(CBT)</h4><span class="arrow-line"></span></div>
  <div class="abs card" style="left:498px"><div class="pic" role="img" aria-label="Two women in a mindfulness class" style="background:linear-gradient(135deg,#b9a7a0,#d8c4b8 50%,#c55a6a)"></div><h4>Mindfulness-Based Cognitive Therapy<br>(MBCT)</h4><span class="arrow-line"></span></div>
  <div class="abs card" style="left:734px"><div class="pic" role="img" aria-label="Silhouette meditating at sunset" style="background:radial-gradient(circle at 50% 40%,#f4e7a8,#8f8450 45%,#2b2a1f)"></div><h4>Mindfulness-Based Stress Reduction<br>(MBSR)</h4><span class="arrow-line"></span></div>
  <div class="abs center" style="top:318px;text-align:center"><span class="btn">Book an appointment</span></div>
  <svg class="abs" style="left:0;bottom:0" width="1200" height="30" viewBox="0 0 1200 30"><polygon points="0,4 740,30 0,30" fill="var(--orange)"/><polygon points="740,30 1200,16 1200,30" fill="var(--white)"/></svg>
</section>

<section class="section therapist">
  <p class="abs script center" style="top:44px;text-align:center">Tips of the day</p>
  <h2 class="abs h2 center" style="top:64px;text-align:center">What say Therapist</h2>
  <span class="chev left" style="left:210px;top:250px"></span>
  <span class="chev right" style="left:980px;top:250px"></span>
  <div class="abs doc-pill" role="img" aria-label="Portrait of a psychologist in a white coat"></div>
  <div class="abs doc">
    <h3>Dr. Orvand</h3>
    <p class="role">Psychologist with 12 years experience</p>
    <p class="para" style="margin-bottom:12px">Lorem ipsum dolor sit amet, consectetur adipiscing elit, sed do eiusmod tempor incididunt ut labore et dolore magna aliqua. Lorem ipsum dolor sit amet, consectetur adipiscing elit, sed do eiusmod tempor incididunt ut labore et dolore magna aliqua.</p>
    <p class="para" style="margin-bottom:14px">Lorem ipsum dolor sit amet, consectetur adipiscing elit, sed do eiusmod tempor incididunt ut labore et dolore magna aliqua.</p>
    <ul class="ticks"><li>Drug Abuse Prevention and Treatment</li><li>Assessment Consultation &amp; Treatment</li><li>Biofeedback and Health Psychology</li><li>Child, Adolescent and Family Services</li></ul>
    <span class="btn" style="margin-top:10px">Read more</span>
  </div>
</section>

<section class="section success">
  <div class="abs success-photo" role="img" aria-label="Therapist listening to a patient, teal tinted"></div>
  <p class="abs script center" style="top:36px;text-align:center;color:var(--white)">Thousands of people get benefit</p>
  <h2 class="abs h2 center" style="top:56px;text-align:center;color:var(--white);font-size:24px">Success Stories of our Patients</h2>
  <span class="abs bubble" style="left:320px;top:226px;width:26px;height:26px"></span>
  <span class="abs bubble" style="left:352px;top:258px;width:14px;height:14px"></span>
  <span class="abs bubble" style="left:846px;top:236px;width:16px;height:16px"></span>
  <div class="abs story">
    <p style="font-size:11px;font-weight:500;margin-bottom:10px">Mira Tello</p>
    <p class="para" style="font-size:9px;line-height:14px">Lorem ipsum dolor sit amet, consectetur adipiscing elit, sed do eiusmod tempor incididunt ut labore et dolore magna aliqua. Lorem ipsum dolor sit amet, consectetur adipiscing elit, sed do eiusmod tempor incididunt ut labore et dolore magna aliqua. Lorem ipsum dolor sit amet.</p>
  </div>
  <div class="abs avatar" role="img" aria-label="Patient portrait"></div>
  <span class="chev left" style="left:358px;top:196px;border-color:var(--white)"></span>
  <span class="chev right" style="left:830px;top:196px;border-color:var(--white)"></span>
  <div class="abs stats"><div><b>132</b><span>Happy Patients</span></div><div><b>16</b><span>Expert Therapist</span></div><div><b>9</b><span>Award Winner</span></div></div>
</section>

<section class="section news">
  <h2 class="abs h2 center" style="top:22px;text-align:center">Our Latest News</h2>
  <article class="abs post" style="left:160px"><div class="pic" role="img" aria-label="Couple talking at a seaside table"><span class="date">02<br>Aug</span></div><h4>5 Strategies To Help You Build Healthy Mind</h4><p class="para" style="font-size:9px;line-height:15px">Lorem ipsum dolor sit amet, consectetur adipiscing elit, sed do eiusmod tempor incididunt ut labore et dolore magna aliqua. <span class="more">Read More</span></p></article>
  <article class="abs post" style="left:459px"><div class="pic" role="img" aria-label="Couple talking at a seaside table"><span class="date">02<br>Aug</span></div><h4>5 Strategies To Help You Build Healthy Mind</h4><p class="para" style="font-size:9px;line-height:15px">Lorem ipsum dolor sit amet, consectetur adipiscing elit, sed do eiusmod tempor incididunt ut labore et dolore magna aliqua. <span class="more">Read More</span></p></article>
  <article class="abs post" style="left:760px"><div class="pic" role="img" aria-label="Couple talking at a seaside table"><span class="date">02<br>Aug</span></div><h4>5 Strategies To Help You Build Healthy Mind</h4><p class="para" style="font-size:9px;line-height:15px">Lorem ipsum dolor sit amet, consectetur adipiscing elit, sed do eiusmod tempor incididunt ut labore et dolore magna aliqua. <span class="more">Read More</span></p></article>
  <div class="abs center" style="top:322px;text-align:center"><span class="btn">Read all news</span></div>
  <svg class="abs" style="left:0;bottom:0" width="1200" height="30" viewBox="0 0 1200 30"><polygon points="470,12 1200,0 1200,26" fill="var(--orange)"/></svg>
</section>

<section class="section appoint">
  <div class="abs services">
    <h3>Our Services for</h3>
    <div class="svc"><i></i><span>Individual<br>Therapy</span></div>
    <div class="svc"><i></i><span>Couples<br>Therapy</span></div>
    <div class="svc"><i></i><span>Group<br>Therapy</span></div>
    <div class="svc"><i></i><span>Child<br>Therapy</span></div>
  </div>
  <div class="abs form">
    <h3>Make an Appointment</h3>
    <div class="row"><div class="field">Name</div><div class="field">Email</div></div>
    <div class="row"><div class="field">Phone</div><div class="field">Subject</div></div>
    <div class="row"><div class="field">Select Date</div><div class="field">Select Time</div></div>
    <div class="row"><div class="field">Address</div></div>
    <div class="row"><div class="field tall">Message</div></div>
    <span class="btn">Book now</span>
  </div>
</section>

<footer class="section footer">
  <div class="abs f-brand"><div style="display:flex;align-items:center;gap:8px;height:34px"><span class="brand-mark"></span><span class="brand-name" style="color:var(--white)">MBC</span></div><div style="font-size:7px;letter-spacing:1px;color:var(--teal-soft);text-transform:uppercase;margin-top:4px">meadowlight balance care</div></div>
  <div class="abs f-contact"><p>Address goes here<br>NY-210</p><p>+1 555 010 2040</p><p>info@mbc.care</p></div>
  <div class="abs" style="left:403px;top:40px"><h5>Links</h5><ul><li>Home</li><li>About Us</li><li>Staff</li><li>Patients</li><li>Treatment</li><li>Contact Us</li></ul></div>
  <div class="abs" style="left:628px;top:40px;width:200px"><h5>Treatments</h5><ul style="line-height:12px"><li style="margin-bottom:9px">Cognitive Behavioral Therapy (CBT)</li><li style="margin-bottom:9px">Mindfulness-Based Cognitive Therapy (MBCT)</li><li style="margin-bottom:9px">Mindfulness-Based Stress Reduction (MBSR)</li><li style="margin-bottom:9px">Anti-Stress Therapy</li><li>Post-Divorce Therapy</li></ul></div>
  <div class="abs" style="left:852px;top:40px"><h5>Follow Us On</h5><ul class="soc"><li>\ Circlepage</li><li>\ Snapframe</li><li>\ Chirpline</li><li>\ Streamhall</li></ul></div>
  <p class="abs copy">&copy; 2022 MBC Therapy. All Right Reserved &nbsp;|&nbsp; Terms &amp; Privacy</p>
</footer>

</body>
</html>
```